Business Card Design

We are a commercial real estate brokerage in San Francisco, leasing office buildings downtown.
I would like a clean, elegant look. Simple but powerful .

Industry/Entity Type

Business

Contact Information for Business Card

Colin Farrow
lic# 07281549
415.555.0172
colin@tarvo-commercial.example
tarvo-commercial.example

```html
<!DOCTYPE html>
<html lang="en">
<head>
<meta charset="utf-8">
<title>Tarvo Commercial – Colin Farrow</title>
<link rel="stylesheet" href="https://fonts.googleapis.com/css2?family=Mulish:wght@400;700&display=swap">
<style>
  :root {
    --slate: #7686a2;
    --graphite: #666666;
    --paper: #ffffff;
  }
  html, body {
    margin: 0;
    padding: 0;
    overflow: hidden;
    background: var(--paper);
  }
  .card {
    position: relative;
    width: 1200px;
    height: 702px;
    background: var(--paper);
    font-family: "Mulish", "Century Gothic", sans-serif;
    overflow: hidden;
  }
  .brand {
    position: absolute;
    top: 122px;
    left: 0;
    width: 1200px;
    display: flex;
    justify-content: center;
    align-items: center;
    gap: 26px;
  }
  .brand-square {
    width: 96px;
    height: 96px;
    background: var(--slate);
  }
  .brand-name {
    color: var(--slate);
    font-weight: 700;
    line-height: 1;
    text-transform: uppercase;
  }
  .brand-name .primary {
    display: block;
    font-size: 80px;
    letter-spacing: 2px;
  }
  .brand-name .secondary {
    display: block;
    font-size: 36px;
    letter-spacing: 1px;
    margin-top: 6px;
  }
  .agent {
    position: absolute;
    top: 386px;
    right: 736px;
    text-align: right;
  }
  .agent-name {
    margin: 0;
    color: var(--slate);
    font-weight: 700;
    font-size: 31px;
    letter-spacing: 0.5px;
    line-height: 1.1;
    text-transform: uppercase;
  }
  .agent-license {
    margin: 0;
    color: var(--graphite);
    font-size: 31px;
    line-height: 1.1;
  }
  .contact {
    position: absolute;
    top: 380px;
    left: 540px;
    margin: 0;
    padding: 0;
    list-style: none;
  }
  .contact-item {
    display: flex;
    align-items: center;
    height: 51px;
    color: var(--graphite);
    font-size: 31px;
  }
  .contact-icon {
    width: 28px;
    height: 28px;
    margin-right: 29px;
    flex: none;
  }
</style>
</head>
<body>
  <main class="card">
    <header class="brand">
      <div class="brand-square"></div>
      <div class="brand-name">
        <span class="primary">Tarvo</span>
        <span class="secondary">Commercial</span>
      </div>
    </header>

    <section class="agent">
      <p class="agent-name">Colin Farrow</p>
      <p class="agent-license">lic# 07281549</p>
    </section>

    <ul class="contact">
      <li class="contact-item">
        <svg class="contact-icon" viewBox="0 0 24 24" aria-hidden="true">
          <path fill="#7686a2" d="M6.6 10.8c1.4 2.8 3.8 5.1 6.6 6.6l2.2-2.2c.3-.3.7-.4 1-.2 1.1.4 2.3.6 3.6.6.6 0 1 .4 1 1V20c0 .6-.4 1-1 1C10.6 21 3 13.4 3 4c0-.6.4-1 1-1h3.5c.6 0 1 .4 1 1 0 1.3.2 2.5.6 3.6.1.3 0 .7-.2 1l-2.3 2.2z"/>
        </svg>
        415.555.0172
      </li>
      <li class="contact-item">
        <svg class="contact-icon" viewBox="0 0 24 24" aria-hidden="true">
          <rect x="1.5" y="5" width="21" height="14" fill="#7686a2"/>
          <path d="M2 5.5l10 7.5 10-7.5M2 18.5l7.5-6.5M22 18.5l-7.5-6.5" fill="none" stroke="#ffffff" stroke-width="1.4"/>
        </svg>
        colin@tarvo-commercial.example
      </li>
      <li class="contact-item">
        <svg class="contact-icon" viewBox="0 0 24 24" aria-hidden="true">
          <g fill="none" stroke="#7686a2" stroke-width="1.6">
            <circle cx="12" cy="12" r="10"/>
            <ellipse cx="12" cy="12" rx="4.5" ry="10"/>
            <path d="M2 12h20M3.5 7h17M3.5 17h17M12 2v20"/>
          </g>
        </svg>
        tarvo-commercial.example
      </li>
    </ul>
  </main>
</body>
</html>
```